QV - menu design

Hi,

We require elegant menu design for upscale restaurant. Please find attached the logo and the menu items for your reference.

for inspiration, this is a good website: -
http://www.platewhisper.example/bellfoldnotes/about.php

We are very much open for Menu Size suggestions.

unfortunately the place is going under renovation, we don't have updated images to it. the closest look and feel to our place is http://varnelo.example ..

we are also open for creative options on the shape, the styles, etc. as long as it represents the fine dine feel ...

Thanks ...

Dear All,

We wouldlike to extend our apology for not being able to provide feedbacks on everysingle design. We were extremely busy and we have multiple contests opensimultaneously which makes the process even harder.

However,we would like to thank you all for the efforts you have put into designingour menu. It is very much appreciated …

We wishyou all success in your design ventures and we are quite positive that we willbe working with many of you on many projects in the soon future. 

Thanks & Regards,

TLG Team...

 

 

 

Industry/Entity Type

Restaurant

Requirements
Must have
• Please ensure that there are 'some' images in the menu ... this is very important.
Should not have
• IMPORTANT: -

1. Please DO NOT insert any currency sign to the menu
2. Please keep the prices of the menu at the end of the menu items descriptions NOT beside the menu item names. The font of the price should be similar to the menu item description and please DO NOT bold the numbers. the prices should be subtle.

Thank you ...

```html
<!DOCTYPE html>
<html lang="en">
<head>
<meta charset="utf-8">
<title>QV – Menu Cover</title>
<link rel="stylesheet" href="https://fonts.googleapis.com/css2?family=Michroma&display=swap">
<style>
  :root {
    --stage: #000000;
    --paper: #f4f4f2;
    --ink: #2a2624;
    --bronze: #a88a6a;
  }
  * { margin: 0; padding: 0; box-sizing: border-box; }
  html, body {
    width: 1200px;
    height: 1000px;
    overflow: hidden;
    background: var(--stage);
  }
  .canvas {
    position: relative;
    width: 1200px;
    height: 1000px;
    background: var(--stage);
  }
  .menu-cover {
    position: absolute;
    left: 440px;
    top: 33px;
    width: 304px;
    height: 927px;
    background: var(--paper);
  }
  .cover-stripes {
    position: absolute;
    left: 0;
    top: 0;
    width: 304px;
    height: 927px;
  }
  .stripe-ink { fill: var(--ink); }
  .stripe-bronze { fill: var(--bronze); }
  .brand-name {
    position: absolute;
    left: 0;
    top: 300px;
    width: 304px;
    text-align: center;
    font-family: "Michroma", sans-serif;
    font-weight: 400;
    color: var(--ink);
    line-height: 1;
  }
  .brand-name .brand-main {
    display: block;
    font-size: 19px;
    letter-spacing: 3px;
  }
  .brand-name .brand-sub {
    display: block;
    margin-top: 10px;
    font-size: 9px;
    letter-spacing: 4px;
  }
</style>
</head>
<body>
  <main class="canvas">
    <section class="menu-cover">
      <svg class="cover-stripes" width="304" height="927" viewBox="0 0 304 927" aria-hidden="true">
        <!-- upper stripe group -->
        <rect class="stripe-ink" x="135" y="0" width="3" height="222"/>
        <rect class="stripe-ink" x="146" y="0" width="3" height="222"/>
        <rect class="stripe-bronze" x="158" y="0" width="3" height="222"/>
        <!-- lower stripe group -->
        <rect class="stripe-ink" x="137" y="370" width="3" height="557"/>
        <rect class="stripe-ink" x="150" y="370" width="3" height="557"/>
        <rect class="stripe-bronze" x="163" y="370" width="3" height="557"/>
      </svg>
      <h1 class="brand-name">
        <span class="brand-main">QUARRY VINE</span>
        <span class="brand-sub">CAFÉ</span>
      </h1>
    </section>
  </main>
</body>
</html>
```